Property Investor needs business card

Hi, we need a business card/logo/email footer/letterhead for a small family property investment business (based in Australia), to just give things a bit more of a professional "look".
Saying that, the property manager is in his late 30s, and is a fun, interesting guy so it doesn't have to be too "corporate" and serious.
Going with eg an 8cmx4cm card size could also make it a bit more interesting. Colour-wise - am relaxed.
Also, the property isn't so much "residential" ie houses/apartments, more "commercial" ie factories, office buildings, shops - in case that helps?
Lastly, the business name is "QHT", so you could also try to do something with those letters.
Enjoy!

```html
<!DOCTYPE html>
<html lang="en">
<head>
<meta charset="UTF-8">
<title>QHT Business Card</title>
<link href="https://fonts.googleapis.com/css2?family=Arimo:ital,wght@0,400;0,700;1,400;1,700&display=swap" rel="stylesheet">
<style>
  :root {
    --backdrop: #e8e5e0;
    --card: #ffffff;
    --green: #7dc242;
    --teal: #1f6b5f;
    --ink: #111111;
    --grey-light: #f4f4f4;
    --grey-mid: #bdbdbd;
    --square: #4cbf7a;
  }
  * { margin: 0; padding: 0; box-sizing: border-box; }
  html, body {
    width: 1200px;
    height: 900px;
    overflow: hidden;
    background: var(--backdrop);
    font-family: "Arimo", Arial, sans-serif;
  }
  .stage { position: relative; width: 1200px; height: 900px; }
  .card {
    position: absolute;
    left: 240px;
    width: 720px;
    height: 360px;
    background: var(--card);
    overflow: hidden;
    box-shadow: 0 6px 18px rgba(0,0,0,0.18);
  }
  .card--front { top: 50px; }
  .card--back { top: 470px; }

  /* front */
  .front-brand {
    position: absolute;
    left: 200px;
    top: 120px;
    display: flex;
    align-items: center;
    gap: 16px;
  }
  .brand-square {
    width: 26px; height: 26px;
    background: var(--teal);
  }
  .brand-name {
    font-weight: 700;
    font-size: 76px;
    letter-spacing: 2px;
    color: var(--green);
    line-height: 1;
  }
  .front-photo {
    position: absolute;
    left: 526px;
    top: 120px;
    width: 194px;
    height: 176px;
    background: linear-gradient(160deg, #f2f2f2 0%, #c9c9c9 100%);
  }
  .front-band-wedge {
    position: absolute;
    left: 0; bottom: 22px;
    width: 526px; height: 40px;
  }
  .front-band {
    position: absolute;
    left: 0; bottom: 0;
    width: 100%; height: 22px;
    background: var(--teal);
  }

  /* back */
  .back-top-band {
    position: absolute;
    left: 0; top: 0;
    width: 520px; height: 24px;
    background: var(--teal);
  }
  .back-logo-box {
    position: absolute;
    right: 0; top: 0;
    width: 200px; height: 180px;
    background: linear-gradient(160deg, #f6f6f6 0%, #c4c4c4 100%);
    display: flex;
    align-items: center;
    justify-content: center;
    gap: 10px;
  }
  .back-logo-box .brand-name { font-size: 52px; }
  .back-logo-box .brand-square { width: 18px; height: 18px; }
  .name-bar {
    position: absolute;
    left: 0; top: 108px;
    width: 420px; height: 64px;
    background: var(--green);
  }
  .holder-name {
    position: absolute;
    left: 34px; top: 118px;
    font-weight: 700;
    font-size: 38px;
    color: #ffffff;
  }
  .holder-title {
    position: absolute;
    left: 42px; top: 176px;
    font-style: italic;
    font-weight: 700;
    font-size: 22px;
    color: var(--ink);
  }
  .accent-square {
    position: absolute;
    left: 548px; top: 206px;
    width: 32px; height: 32px;
    background: var(--square);
  }
  .contact-list {
    position: absolute;
    left: 58px; top: 228px;
    list-style: none;
  }
  .contact-item {
    display: flex;
    align-items: center;
    gap: 14px;
    height: 36px;
    font-size: 17px;
    color: var(--ink);
  }
  .contact-icon { width: 18px; height: 18px; fill: var(--teal); }
</style>
</head>
<body>
<main class="stage">
  <section class="card card--front" aria-label="Business card front">
    <div class="front-brand">
      <span class="brand-name">QHT</span>
      <span class="brand-square"></span>
    </div>
    <div class="front-photo" role="img" aria-label="Rendered photo of a commercial property"></div>
    <svg class="front-band-wedge" viewBox="0 0 526 40" preserveAspectRatio="none" aria-hidden="true">
      <polygon points="0,40 526,40 526,0" fill="#ffffff"/>
    </svg>
    <div class="front-band"></div>
  </section>

  <section class="card card--back" aria-label="Business card back">
    <div class="back-top-band"></div>
    <div class="back-logo-box">
      <span class="brand-name">QHT</span>
      <span class="brand-square"></span>
    </div>
    <div class="name-bar"></div>
    <p class="holder-name">Your Name</p>
    <p class="holder-title">Job Title</p>
    <div class="accent-square"></div>
    <ul class="contact-list">
      <li class="contact-item">
        <svg class="contact-icon" viewBox="0 0 24 24" aria-hidden="true"><path d="M12 2a7 7 0 0 0-7 7c0 5 7 13 7 13s7-8 7-13a7 7 0 0 0-7-7zm0 9.5A2.5 2.5 0 1 1 12 6.5a2.5 2.5 0 0 1 0 5z"/></svg>
        Your House, Your Street, Town, Country-Postcode
      </li>
      <li class="contact-item">
        <svg class="contact-icon" viewBox="0 0 24 24" aria-hidden="true"><path d="M7 1h10a2 2 0 0 1 2 2v18a2 2 0 0 1-2 2H7a2 2 0 0 1-2-2V3a2 2 0 0 1 2-2zm0 3v11h10V4zm2 13v2h2v-2zm4 0v2h2v-2z"/></svg>
        0123 564789
      </li>
      <li class="contact-item">
        <svg class="contact-icon" viewBox="0 0 24 24" aria-hidden="true"><path d="M2 5h20v14H2zm2 2v.4l8 5.2 8-5.2V7zm0 2.8V17h16V9.8l-8 5.2z"/></svg>
        you@yourmail.com
      </li>
    </ul>
  </section>
</main>
</body>
</html>
```